Solar and energy efficient equipment finance introduction and product flyer

Were a specialty provider of finance solutions for solar and energy efficient equipment. Our customers (the people and businesses that get the equipment installed on their properties) use our solutions to get equipment for $0 upfront. Even better then paying nothing upfront, they can often pay for the systems via the savings generated - meaning they are cash flow positive immediately.

The attached presentation is to introduce OUR FIRM to solar and energy efficient equipment retailers and installers (our distributors). These distributors then offer our finance to their customers to help secure sales.

As such the audience for this document is solar installers and distributors. We are looking for a fresh look that says:

- we get understand the technology,
- we're agile and highly responsive,
- we create unique value adding solutions, and
- we're totally reliable.

We also want to update the attached flyer(s) to match stylistically. In this instance the template will introduce OUR PRODUCTS to distributor AND customers.

Target Market(s)

Solar and energy efficient equipment finance retailers and installers

Industry/Entity Type

Finance

Font styles to use
Serif

Colors
f37022
0255a3

Requirements
Must have
• Template functionality

```html
<!DOCTYPE html>
<html lang="en">
<head>
<meta charset="utf-8">
<title>Flexibility – Northvale Capital</title>
<link rel="stylesheet" href="https://fonts.googleapis.com/css2?family=Inter:wght@500;900&family=Roboto+Condensed:wght@700&display=swap">
<style>
  :root {
    --sky-top: #2f86cf;
    --sky-mid: #a9c9e6;
    --mist: #e4e6ef;
    --mist-bottom: #dcdde8;
    --banner-white: #ffffff;
    --banner-shadow: #262a66;
    --accent-red: #e8232a;
    --ink: #000000;
  }
  * { margin: 0; padding: 0; box-sizing: border-box; }
  html, body { width: 1200px; height: 927px; overflow: hidden; }
  body { background: var(--mist); }

  .flyer {
    position: relative;
    width: 1200px;
    height: 927px;
    overflow: hidden;
    background: linear-gradient(180deg, var(--sky-top) 0%, var(--sky-mid) 22%, var(--mist) 48%, var(--mist-bottom) 100%);
    font-family: "Inter", Arial, sans-serif;
  }

  .backdrop-pattern {
    position: absolute;
    inset: 0;
    background:
      radial-gradient(circle at 1020px 290px, rgba(190, 170, 200, 0.22) 0 190px, transparent 260px),
      radial-gradient(circle at 210px 700px, rgba(170, 200, 210, 0.25) 0 200px, transparent 280px),
      radial-gradient(circle at 520px 720px, rgba(170, 190, 230, 0.18) 0 180px, transparent 260px);
  }

  .tagline-banner {
    position: absolute;
    left: 0;
    top: 21px;
    width: 1121px;
    height: 126px;
    background: var(--banner-white);
    box-shadow: 18px 14px 0 var(--banner-shadow);
    display: flex;
    align-items: center;
    padding-left: 45px;
  }
  .tagline-dot {
    width: 31px;
    height: 31px;
    border-radius: 50%;
    background: var(--accent-red);
    margin-right: 18px;
    flex: none;
  }
  .tagline-text {
    font-family: "Roboto Condensed", "Arial Narrow", sans-serif;
    font-weight: 700;
    font-size: 72px;
    letter-spacing: 0.6px;
    color: var(--accent-red);
    line-height: 1;
    white-space: nowrap;
  }

  .headline {
    position: absolute;
    left: 220px;
    top: 318px;
    font-family: "Inter", Arial, sans-serif;
    font-weight: 900;
    font-size: 112px;
    line-height: 94px;
    letter-spacing: -3px;
    color: var(--ink);
    white-space: nowrap;
  }

  .brand-name {
    position: absolute;
    right: 72px;
    top: 846px;
    font-family: "Inter", Arial, sans-serif;
    font-weight: 500;
    font-size: 36px;
    letter-spacing: -0.5px;
    color: var(--ink);
    white-space: nowrap;
  }
</style>
</head>
<body>
  <main class="flyer">
    <div class="backdrop-pattern" role="img" aria-label="Faint decorative rings and crosshatch lines in soft pastel tones"></div>

    <header class="tagline-banner">
      <span class="tagline-dot"></span>
      <p class="tagline-text">we're agile and highly responsive</p>
    </header>

    <h1 class="headline">The flexibility<br>to offer a<br>range of<br>solutions</h1>

    <footer class="brand-name">Northvale Capital</footer>
  </main>
</body>
</html>
```